Print on top the name of the company: (Or Similar)
Larkmoor Cleaning & Disinfecting
Because your standards aren't standard.

We adhere to ALL NVB guidelines for both residential and commercial cleaning.

Infection Control is our ultimate goal.

Instructions:
Opening a residential and commercial cleaning and disinfecting company in south Florida.

Targeting high-end residential clients, commercial and healthcare facilities, specializing in Ambulatory Care Guidelines. With a concentration and expertise in targeting Covid 19 and other transmissible pathogens.

UMRE trained.
Owned and operated by a licensed BSN Registered Nurse specially ​trained in Infection Control Prevention with over 25 years experience. Over two decades in Ambulatory Surgery Center Administration, Director of Nursing and Infection Control Prevention ad Consulting.

Looking to create a business flier that emphasizes Cleaning & Disinfection
along with the standard expectation for residential and Commercial cleaning services
Updates

Need extra days to review

Target Market(s)

Residential & Commercial

Font styles to use
Decorative

Requirements
Must have
• A checklist for cleaning services

```html
<!DOCTYPE html>
<html lang="en">
<head>
<meta charset="utf-8">
<title>Larkmoor Cleaning &amp; Disinfecting – Flyer</title>
<link href="https://fonts.googleapis.com/css2?family=Roboto+Condensed:wght@400;500;700&display=swap" rel="stylesheet">
<style>
  :root {
    --yellow: #FFD23F;
    --yellow-deep: #F6B91A;
    --blue: #0A84C6;
    --blue-title: #0B6FB0;
    --ink: #1B1B1B;
    --white: #FFFFFF;
    --page: #ECEBE8;
  }
  html, body {
    margin: 0; padding: 0;
    width: 1200px; height: 1200px;
    overflow: hidden;
    background: var(--page);
    font-family: "Roboto Condensed", "Arial Narrow", sans-serif;
  }
  .flyer {
    position: absolute;
    left: 194px; top: 30px;
    width: 812px; height: 1140px;
    background: var(--white);
    overflow: hidden;
    color: var(--ink);
  }
  .flyer-shapes { position: absolute; inset: 0; }
  .photo {
    position: absolute;
    border-radius: 50%;
    box-sizing: border-box;
  }
  .photo--main {
    left: 404px; top: 22px; width: 500px; height: 500px;
    background: radial-gradient(circle at 60% 40%, #F2EEE8 0%, #C9C5BF 55%, #8C8D90 100%);
    border: 8px solid var(--white);
  }
  .photo--floor {
    left: 352px; top: 388px; width: 216px; height: 216px;
    background: linear-gradient(180deg, #CFE3EF 0%, #9CC6DF 60%, #BFD9E8 100%);
    border: 5px solid var(--white);
  }
  .photo--vacuum {
    left: 520px; top: 480px; width: 180px; height: 180px;
    background: linear-gradient(180deg, #F3F1EC 0%, #E2DCD2 65%, #B8A994 100%);
    border: 5px solid var(--white);
  }
  .title {
    position: absolute; left: 38px; top: 150px;
    margin: 0;
    font-weight: 700; font-size: 58px; line-height: 55px;
    letter-spacing: -1px;
    text-transform: uppercase;
  }
  .title-name { color: var(--ink); display: block; }
  .title-service { color: var(--blue-title); display: block; }
  .title-amp { color: var(--ink); }
  .tagline {
    position: absolute; left: 38px; top: 340px; margin: 0;
    font-size: 25px; line-height: 32px; font-weight: 400;
  }
  .intro {
    position: absolute; left: 38px; top: 510px; margin: 0;
    font-size: 25px; line-height: 32px; font-weight: 400;
  }
  .intro-note {
    position: absolute; left: 38px; top: 618px; margin: 0;
    font-size: 18px; font-weight: 400;
  }
  .services-tab {
    position: absolute; left: 250px; top: 690px; width: 316px; height: 50px;
    display: flex; align-items: center; justify-content: center;
    font-weight: 700; font-size: 30px; color: var(--ink); margin: 0;
  }
  .service-group { position: absolute; top: 772px; }
  .service-group--commercial { left: 38px; }
  .service-group--residential { left: 442px; }
  .service-heading {
    margin: 0 0 12px; color: var(--yellow);
    font-weight: 700; font-size: 21px;
  }
  .service-columns { display: flex; }
  .checklist {
    list-style: none; margin: 0; padding: 0;
    color: var(--white); font-size: 16px; line-height: 20px;
  }
  .service-group--commercial .checklist:first-child { width: 180px; }
  .service-group--residential .checklist:first-child { width: 157px; }
  .checklist li {
    position: relative; padding-left: 18px; margin-bottom: 8px;
  }
  .checklist li::before {
    content: ""; position: absolute; left: 0; top: 5px;
    width: 10px; height: 10px; border-radius: 50%;
    background: var(--yellow);
  }
  .call-to-action {
    position: absolute; left: 38px; top: 1028px; margin: 0;
    font-size: 21px; line-height: 28px; text-transform: uppercase;
  }
  .contact { position: absolute; left: 516px; top: 1044px; }
  .contact-phone {
    display: flex; align-items: center; gap: 14px;
    font-weight: 700; font-size: 33px; margin: 0;
  }
  .contact-web {
    display: flex; align-items: center; gap: 14px;
    font-size: 17px; margin: 6px 0 0;
  }
  .icon { width: 24px; height: 24px; flex: none; }
  .icon--small { width: 18px; height: 18px; margin-left: 3px; margin-right: 3px; }
</style>
</head>
<body>
<main class="flyer">
  <svg class="flyer-shapes" width="812" height="1140" viewBox="0 0 812 1140" aria-hidden="true">
    <rect x="0" y="0" width="812" height="720" fill="var(--yellow)"/>
    <path d="M0,0 H548 C440,70 330,125 230,120 C130,115 50,95 0,72 Z" fill="var(--white)"/>
    <path d="M0,486 C90,434 200,420 300,434 C380,446 424,474 470,512" fill="none" stroke="var(--yellow-deep)" stroke-width="8"/>
    <path d="M0,494 C90,442 200,428 300,442 C380,454 420,482 470,522 L812,570 L812,1140 L0,1140 Z" fill="var(--white)"/>
    <circle cx="654" cy="272" r="262" fill="none" stroke="var(--blue)" stroke-width="10"/>
    <path d="M700,540 C740,548 780,545 812,538 V556 C780,566 740,566 700,556 Z" fill="var(--blue)"/>
    <path d="M690,565 C740,572 780,568 812,560 V572 C780,582 740,582 690,575 Z" fill="var(--yellow)"/>
    <path d="M0,702 H812 V968 C720,955 640,960 560,975 C420,995 200,994 0,994 Z" fill="var(--blue)"/>
    <path d="M216,702 H598 L590,714 V730 Q590,740 580,740 H236 Q226,740 226,730 V714 Z" fill="var(--yellow)"/>
    <path d="M210,702 H598 L606,690 H210 Z" fill="var(--yellow-deep)"/>
    <line x1="406" y1="778" x2="406" y2="950" stroke="var(--white)" stroke-width="1.5" stroke-dasharray="2 4" opacity="0.7"/>
    <path d="M0,1140 V1110 C200,1130 420,1098 560,1040 C660,998 740,975 812,972 V1140 Z" fill="var(--yellow)"/>
    <path d="M300,1140 C450,1120 600,1080 812,1000" fill="none" stroke="#EDEDED" stroke-width="6"/>
  </svg>

  <div class="photo photo--main" role="img" aria-label="Photo of a smiling cleaner in gloves wiping a kitchen oven"></div>
  <div class="photo photo--floor" role="img" aria-label="Photo of a worker mopping a shiny commercial floor"></div>
  <div class="photo photo--vacuum" role="img" aria-label="Photo of a man vacuuming a carpet at home"></div>

  <h1 class="title">
    <span class="title-name">Larkmoor</span>
    <span class="title-service">Cleaning <span class="title-amp">&amp;</span></span>
    <span class="title-service">Disinfecting</span>
  </h1>
  <p class="tagline">Because your standards<br>aren't standard</p>

  <p class="intro">We do all NVB guidelines<br>for both residential and<br>commercial cleaning</p>
  <p class="intro-note">Infection control is our ultimate goal</p>

  <h2 class="services-tab">OUR SERVICES</h2>

  <section class="service-group service-group--commercial">
    <h3 class="service-heading">SPARKLING CLEANING</h3>
    <div class="service-columns">
      <ul class="checklist">
        <li>Commercial</li><li>Janitorial</li><li>Offices</li><li>Floor maintenance</li><li>Carpet cleaning</li>
      </ul>
      <ul class="checklist">
        <li>Move-ins</li><li>Move-outs</li><li>Constructions<br>clean-ups</li><li>Estate clean-outs</li>
      </ul>
    </div>
  </section>

  <section class="service-group service-group--residential">
    <h3 class="service-heading">RESIDENTAL</h3>
    <div class="service-columns">
      <ul class="checklist">
        <li>House cleaning</li><li>Before and<br>after party</li><li>Move-ins</li><li>Move-outs</li>
      </ul>
      <ul class="checklist">
        <li>Holiday cleaning</li><li>Seasonal cleaning</li><li>Carpet cleaning</li><li>Deodorizing and<br>sanitizing</li>
      </ul>
    </div>
  </section>

  <p class="call-to-action">Call us to find out how<br>can save money this month!</p>

  <div class="contact">
    <p class="contact-phone">
      <svg class="icon" viewBox="0 0 24 24" aria-hidden="true"><circle cx="12" cy="12" r="12" fill="var(--blue)"/><path d="M8.2 6.5l2 2.1-1.1 1.6c.8 1.7 2 2.9 3.7 3.7l1.6-1.1 2.1 2-1 1.9c-4.3-.3-8.2-4.2-8.5-8.5z" fill="var(--white)"/></svg>
      (305) 555 0182
    </p>
    <p class="contact-web">
      <svg class="icon icon--small" viewBox="0 0 24 24" aria-hidden="true"><circle cx="12" cy="12" r="10.5" fill="none" stroke="var(--blue)" stroke-width="2"/><ellipse cx="12" cy="12" rx="4.5" ry="10.5" fill="none" stroke="var(--blue)" stroke-width="2"/><line x1="1.5" y1="12" x2="22.5" y2="12" stroke="var(--blue)" stroke-width="2"/></svg>
      www.larkmoorcleaning.com
    </p>
  </div>
</main>
</body>
</html>
```